1. Overview of company:
Copper Lark Mobile solutions private Ltd is one of the leading innovators & providers of Value added services (VAS) and telecom solutions to the top telecom operators across the world. We are the pioneer of several telecom technologies and products with our solutions empowering over 40 telecom giant in 51 countries.

2. Product Overview:
Tonebender is the most innovative voice morphing mobile app that has revolutionized the concept of IVR based offerings for telecom operators across the world. It lets you talk to your friend in a voice of your choice at just the press of a button. In addition to every call, users can now speak to their friends with background sounds of their choice.

In simple words: If person A calls person B, person A can choose the voice he wants B to listen, Words and sentences remain same just the voice changes. Person A can even activate a background sound for both of them while talking.

3. Objective of the design:
The purpose of this campaign is to establish Tonebender as Innovative, Lively, Youthful, Fun mobile app generally used for spreading smiles via pranks. The primary objective is to persuade the audience to download and use Tonebender mobile app, as well as to spread and characterize this new app.

4. Product layout:
Page 1: Landing Page
- pictorial explanation, what Tonebender stands for

Page 2: Home Screen options
-Navigation to tonebender
-Navigation to sound canvas

Page 3: Tonebender options
-Female
-Cartoon
-King
-Bunny

Page 4: Sound Canvas options
-Romantic
-Airport
-Traffic
-Football
-Church
-Beach

5. Target Audience
The users of the mobile app will be teenager whose age ranges from 16-27. The demographics are not restricted to a particular country and will be present on global level.

6. Deliverable
- 4 Uncoded screen and icon for mobile app "Tonebender"
- Our company name is "Copper Lark" , we would like to see designs that use Black and Green, at the same time its not mandatory.
-Design should communicate what the app stands for "Changing voice of caller"

Target Market(s)

User of the mobile app will be teenagers whose age ranges from 16-27. The demographics are not restricted to a particular country and will be present on global level. It's for masses.

Industry/Entity Type

Telecommunications

Requirements
Must have
• The design should be self explanatory, what the app stands for.
• Editable format for integration purpose.
Nice to have
• Would prefer Icons and very few words.
• Professional, elegant at the same time trendy designs.

```html
<!DOCTYPE html>
<html lang="en">
<head>
<meta charset="utf-8">
<title>Voice Morph Screen</title>
<link rel="stylesheet" href="https://fonts.googleapis.com/css2?family=Oswald:wght@400;500;600&family=Roboto:wght@400;500&display=swap">
<style>
  :root {
    --green: #8cc63f;
    --green-dark: #6fa82a;
    --green-soft: #e6f2d6;
    --ink: #3c3c3c;
    --muted: #9a9a9a;
    --line: #d9d9d9;
    --tile: #f4f4f4;
    --screen: #ffffff;
    --stage: #e8ebe4;
  }
  * { box-sizing: border-box; margin: 0; padding: 0; }
  html, body { width: 1200px; height: 800px; overflow: hidden; }
  body {
    background: var(--stage);
    display: flex; align-items: center; justify-content: center;
    font-family: "Oswald", sans-serif; color: var(--ink);
  }
  .app-screen {
    width: 375px; height: 667px; background: var(--screen);
    display: flex; flex-direction: column; position: relative;
    box-shadow: 0 10px 40px rgba(0,0,0,.12);
  }
  .status-bar {
    height: 22px; display: flex; align-items: center; justify-content: space-between;
    padding: 0 8px; font-family: "Roboto", sans-serif; font-size: 11px; color: #222;
  }
  .status-bar .time { font-weight: 500; }
  .status-bar .battery { display: flex; align-items: center; gap: 4px; }
  .battery-icon { width: 22px; height: 10px; border: 1px solid #222; border-radius: 2px; padding: 1px; }
  .battery-icon span { display: block; height: 100%; background: #222; border-radius: 1px; }
  .content { flex: 1; padding: 20px 30px 0; display: flex; flex-direction: column; }
  .section-head {
    display: flex; align-items: center; gap: 12px;
    font-size: 21px; font-weight: 500; color: var(--green); letter-spacing: .3px;
    padding-bottom: 12px; border-bottom: 1px solid var(--line); margin-bottom: 14px;
  }
  .toggle { width: 24px; height: 12px; background: var(--green); border-radius: 6px; position: relative; }
  .toggle::after { content: ""; position: absolute; right: 2px; top: 2px; width: 8px; height: 8px; border-radius: 50%; background: #fff; }
  .picker { display: flex; align-items: flex-start; justify-content: space-between; padding-bottom: 12px; border-bottom: 1px solid var(--line); }
  .chevron { width: 12px; height: 54px; display: flex; align-items: center; }
  .chevron svg { width: 10px; height: 16px; }
  .option { width: 60px; display: flex; flex-direction: column; align-items: center; gap: 6px; }
  .tile {
    width: 54px; height: 54px; background: var(--tile); border: 1px solid var(--line);
    display: flex; align-items: center; justify-content: center;
  }
  .tile svg { width: 30px; height: 30px; fill: none; stroke: var(--ink); stroke-width: 1.6; stroke-linecap: round; stroke-linejoin: round; }
  .option.is-active .tile { background: var(--green); border-color: var(--green); }
  .option.is-active .tile svg { stroke: #fff; }
  .option-label { font-size: 8px; letter-spacing: .6px; color: var(--muted); text-transform: uppercase; }
  .slider-card {
    margin: 18px 0 28px; padding: 10px 14px 12px; background: #fff;
    box-shadow: 0 2px 8px rgba(0,0,0,.14);
  }
  .slider-label { text-align: center; font-size: 10px; font-weight: 500; letter-spacing: .4px; margin-bottom: 6px; }
  .slider-row { display: flex; align-items: center; gap: 10px; color: var(--muted); font-family: "Roboto", sans-serif; font-size: 16px; }
  .track { flex: 1; height: 4px; background: var(--line); border-radius: 2px; }
  .track span { display: block; height: 100%; background: var(--green); border-radius: 2px; }
  .player { margin-top: auto; padding-bottom: 16px; display: flex; flex-direction: column; align-items: center; gap: 4px; }
  .player-state { font-size: 8px; letter-spacing: .8px; color: var(--muted); }
  .player-row { display: flex; align-items: center; gap: 24px; }
  .player-time { font-size: 10px; color: var(--green-dark); width: 30px; text-align: right; }
  .pause { width: 30px; height: 30px; border: 2px solid var(--green-soft); border-radius: 50%; display: flex; align-items: center; justify-content: center; }
  .pause svg { width: 12px; height: 12px; }
  .star svg { width: 22px; height: 22px; }
  .tab-bar { height: 60px; background: var(--green); display: flex; }
  .tab { flex: 1; display: flex; flex-direction: column; align-items: center; justify-content: center; gap: 4px; color: #fff; font-size: 9px; font-weight: 500; letter-spacing: .6px; }
  .tab svg { width: 22px; height: 22px; fill: none; stroke: #fff; stroke-width: 1.6; stroke-linecap: round; stroke-linejoin: round; }
  .tab.is-active { background: #fff; color: var(--green); }
  .tab.is-active svg { stroke: var(--green); }
</style>
</head>
<body>
<main class="app-screen">
  <header class="status-bar">
    <span class="carrier">●●●○○ Carrier</span>
    <span class="time">12:34 AM</span>
    <span class="battery">100% <span class="battery-icon"><span></span></span></span>
  </header>

  <section class="content">
    <h2 class="section-head">CHOOSE YOUR VOICE <span class="toggle"></span></h2>
    <div class="picker voice-picker">
      <span class="chevron"><svg viewBox="0 0 10 16"><path d="M8 2 2 8l6 6" fill="none" stroke="#bbb" stroke-width="1.6"/></svg></span>
      <div class="option">
        <div class="tile"><svg viewBox="0 0 30 30"><path d="M3 15c4-6 8-7 12-4 4-3 8-2 12 4-4 6-8 8-12 8s-8-2-12-8z"/><path d="M3 15h24"/></svg></div>
        <span class="option-label">Female</span>
      </div>
      <div class="option">
        <div class="tile"><svg viewBox="0 0 30 30"><circle cx="15" cy="15" r="11"/><path d="M9 17c2 3 10 3 12 0"/></svg></div>
        <span class="option-label">Cartoon</span>
      </div>
      <div class="option is-active">
        <div class="tile"><svg viewBox="0 0 30 30"><path d="M4 10l5 6 6-8 6 8 5-6-2 13H6z"/><path d="M6 26h18"/></svg></div>
        <span class="option-label">King</span>
      </div>
      <div class="option">
        <div class="tile"><svg viewBox="0 0 30 30"><path d="M11 14V5c0-2 3-2 3 0v9M16 14V5c0-2 3-2 3 0v9"/><rect x="8" y="14" width="14" height="12" rx="5"/></svg></div>
        <span class="option-label">Bunny</span>
      </div>
      <span class="chevron"><svg viewBox="0 0 10 16"><path d="m2 2 6 6-6 6" fill="none" stroke="#8cc63f" stroke-width="1.8"/></svg></span>
    </div>
    <div class="slider-card">
      <p class="slider-label">VOICE DISTORTION LEVEL</p>
      <div class="slider-row"><span>–</span><div class="track"><span style="width:42%"></span></div><span>+</span></div>
    </div>

    <h2 class="section-head">SELECT AN AMBIANCE <span class="toggle"></span></h2>
    <div class="picker ambiance-picker">
      <span class="chevron"><svg viewBox="0 0 10 16"><path d="M8 2 2 8l6 6" fill="none" stroke="#bbb" stroke-width="1.6"/></svg></span>
      <div class="option">
        <div class="tile"><svg viewBox="0 0 30 30"><path d="M15 25S4 18 4 11a5.5 5.5 0 0 1 11-1 5.5 5.5 0 0 1 11 1c0 7-11 14-11 14z"/></svg></div>
        <span class="option-label">Romantic</span>
      </div>
      <div class="option is-active">
        <div class="tile"><svg viewBox="0 0 30 30"><path d="M15 3c1.2 0 1.6 1.5 1.6 3v6l9 5v2.5l-9-2.5v5l3 2.5v2l-4.6-1.3L10.4 26v-2l3-2.5v-5l-9 2.5V17l9-5V6c0-1.5.4-3 1.6-3z"/></svg></div>
        <span class="option-label">Airport</span>
      </div>
      <div class="option">
        <div class="tile"><svg viewBox="0 0 30 30"><rect x="10" y="3" width="10" height="24" rx="3"/><circle cx="15" cy="8" r="2"/><circle cx="15" cy="15" r="2"/><circle cx="15" cy="22" r="2"/><path d="M10 7H6l4 4M10 14H6l4 4M20 7h4l-4 4M20 14h4l-4 4"/></svg></div>
        <span class="option-label">Traffic</span>
      </div>
      <div class="option">
        <div class="tile"><svg viewBox="0 0 30 30"><circle cx="15" cy="15" r="11"/><path d="m15 10 4 3-1.5 5h-5L11 13zM15 10V4M19 13l6-2M17.5 18l3 5M12.5 18l-3 5M11 13l-6-2"/></svg></div>
        <span class="option-label">Stadium</span>
      </div>
      <span class="chevron"><svg viewBox="0 0 10 16"><path d="m2 2 6 6-6 6" fill="none" stroke="#8cc63f" stroke-width="1.8"/></svg></span>
    </div>
    <div class="slider-card">
      <p class="slider-label">AMBIANCE VOLUME</p>
      <div class="slider-row"><span>–</span><div class="track"><span style="width:72%"></span></div><span>+</span></div>
    </div>

    <div class="player">
      <span class="player-state">PLAYING</span>
      <div class="player-row">
        <span class="player-time">0:13</span>
        <span class="pause"><svg viewBox="0 0 12 12"><path d="M3.5 1v10M8.5 1v10" stroke="#6fa82a" stroke-width="1.8"/></svg></span>
        <span class="star"><svg viewBox="0 0 24 24"><path d="m12 2 3 7 7.5.6-5.7 5 1.8 7.4L12 18l-6.6 4 1.8-7.4-5.7-5L9 9z" fill="#8a8a8a"/></svg></span>
      </div>
    </div>
  </section>

  <nav class="tab-bar">
    <a class="tab is-active"><svg viewBox="0 0 24 24"><path d="M3 6h4l10 12h4M3 18h4l10-12h4M18 3l3 3-3 3M18 15l3 3-3 3"/></svg>MORPH</a>
    <a class="tab"><svg viewBox="0 0 24 24"><path d="m12 2 3 7 7.5.6-5.7 5 1.8 7.4L12 18l-6.6 4 1.8-7.4-5.7-5L9 9z"/></svg>SAVED</a>
    <a class="tab"><svg viewBox="0 0 24 24"><rect x="9" y="2" width="6" height="12" rx="3"/><path d="M5 11a7 7 0 0 0 14 0M12 18v4M8 22h8"/></svg>RECORD</a>
    <a class="tab"><svg viewBox="0 0 24 24"><path d="M5 3h4l2 5-2.5 1.5a11 11 0 0 0 6 6L16 13l5 2v4a2 2 0 0 1-2 2A16 16 0 0 1 3 5a2 2 0 0 1 2-2z"/></svg>CALL</a>
  </nav>
</main>
</body>
</html>
```